Andes Pantry Company (importer of Latin American foods)

We seek to be the N1 distributor in Europe with Latin American quality products, we seek a sober catalog design where white and black predominate, with a professional and luxurious appearance. We seek to use an image that characterizes us a lot about Latin American looks and to give information about the brands that we represent from Latin America, we seek to have long-term contact with the designer since it will undergo changes during the first year

Target Market(s)

Retail channel, cash and carry's and distributors

Industry/Entity Type

Supermarket

Font styles to use
Sans Serif

Requirements
Must have
• It has to be a catalog that represents Latin American cultural diversity, the brands that we export from Argentina to Mexico are premium and the catalog must be in accordance with our brands
Nice to have
• Map of Latin America, Photos of Latin America, brief description of our brands, description of our company, black and white typography. Our logo must be on each sheet of the catalog, easily modifiable format to add future brands
Should not have
• We are open to designer suggestions

```html
<!DOCTYPE html>
<html lang="en">
<head>
<meta charset="utf-8">
<title>Andes Pantry Company – Catalogue Spreads</title>
<link href="https://fonts.googleapis.com/css2?family=Roboto:ital,wght@1,300&family=Playfair+Display:wght@800&family=Raleway:wght@200;400;600&display=swap" rel="stylesheet">
<style>
  :root{
    --stage:#e6e6e6;
    --paper:#ffffff;
    --ink:#111111;
    --ink-soft:#555555;
    --rule:#bdbdbd;
    --caption:#2b2b2b;
  }
  *{box-sizing:border-box;margin:0;padding:0}
  html,body{width:1200px;height:1150px;overflow:hidden;background:var(--stage)}
  .board{position:relative;width:1200px;height:1150px;display:grid;grid-template-columns:600px 600px;grid-template-rows:383px 383px 384px}
  .cell{position:relative}
  .caption{position:absolute;right:22px;bottom:20px;font-family:"Roboto",sans-serif;font-style:italic;font-weight:300;font-size:26px;color:var(--caption)}
  .spread{position:absolute;left:70px;top:36px;width:460px;height:230px;display:flex;box-shadow:0 10px 24px rgba(0,0,0,.18)}
  .page{position:relative;width:230px;height:230px;background:var(--paper);overflow:hidden}
  .page--left{border-right:1px solid rgba(0,0,0,.08)}
  .page--dark{background:var(--ink)}
  .map-block{position:absolute;left:50%;top:50%;width:40px;height:30px;transform:translate(-50%,-50%);border-radius:4px}
  .map-block--light{background:#f2f2f2}
  .map-block--dark{background:var(--ink)}
  .brand{position:absolute;display:flex;align-items:center;gap:6px;font-family:"Raleway",sans-serif;font-weight:600;line-height:1.05}
  .brand__dot{border-radius:50%;flex:none}
  .brand--cover{left:50%;top:50%;transform:translate(-50%,-50%);flex-direction:column;gap:8px;font-size:13px;text-align:center;letter-spacing:.04em}
  .brand--cover .brand__dot{width:64px;height:64px}
  .brand--light{color:#fff}
  .brand--light .brand__dot{background:#fff}
  .brand--dark{color:var(--ink)}
  .brand--dark .brand__dot{background:var(--ink)}
  .brand--corner{right:10px;bottom:10px;font-size:5px;color:var(--ink);width:60px;justify-content:flex-end;text-align:right}
  .brand--corner .brand__dot{width:12px;height:12px;background:var(--ink)}
  .photo{position:absolute}
  .photo--corn{left:28px;top:42px;width:160px;height:140px;border-radius:50%;background:radial-gradient(circle at 40% 40%,#d9b25a,#b5473a 45%,#5a3a6e 75%,#2e2a3a)}
  .photo--full{inset:0}
  .photo--churros{background:radial-gradient(circle at 55% 45%,#d99b5a,#9a6232 40%,#3a3532 80%)}
  .photo--mortar{background:radial-gradient(circle at 40% 55%,#c9b8a8,#6f6760 45%,#5a3a2a 80%)}
  .photo--drink{background:radial-gradient(circle at 45% 50%,#e8f0d8,#9cc04a 40%,#3d4a2c 75%,#2a2a2a)}
  .heading-serif{font-family:"Playfair Display",serif;font-weight:800;color:var(--ink)}
  .index__title{position:absolute;left:40px;top:40px;font-size:15px}
  .index__list{position:absolute;left:40px;list-style:none;font-family:"Raleway",sans-serif;font-size:5.5px;color:var(--ink-soft);line-height:1.45}
  .index__list--a{top:72px}
  .index__list--b{top:120px}
  .index__side{position:absolute;right:28px;top:40px;font-family:"Raleway",sans-serif;font-size:5px;letter-spacing:.3em;color:var(--ink-soft)}
  .page--framed{border:9px solid var(--ink)}
  .story__title{position:absolute;left:30px;top:62px;font-size:17px}
  .story__rule{position:absolute;left:30px;top:92px;width:120px;height:1px;background:var(--rule)}
  .body-copy{position:absolute;font-family:"Raleway",sans-serif;font-size:5.5px;line-height:1.55;color:var(--ink-soft)}
  .story__copy{left:30px;top:108px;width:160px}
  .flavors__kicker{position:absolute;left:60px;top:88px;font-family:"Playfair Display",serif;font-size:7px;letter-spacing:.35em;color:var(--ink);text-align:center;width:110px}
  .flavors__title{position:absolute;left:30px;top:106px;font-family:"Raleway",sans-serif;font-weight:200;font-size:19px;letter-spacing:.04em;color:var(--ink)}
  .flavors__copy{left:30px;top:134px;width:150px}
  .product{position:absolute;display:flex;align-items:center;gap:8px}
  .product__art{width:22px;height:22px;border-radius:50%;flex:none}
  .product__label{border:1px solid var(--rule);padding:4px 6px;width:76px;font-family:"Raleway",sans-serif;font-size:4.8px;color:var(--ink-soft);line-height:1.4}
  .product__label strong{display:block;font-weight:600;color:var(--ink);font-size:5px;letter-spacing:.12em;text-transform:uppercase}
  .product--pineapple{left:16px;top:36px}
  .product--strawberry{left:120px;top:58px;flex-direction:row-reverse}
  .product--lime{left:16px;top:104px}
  .product--coconut{left:120px;top:126px;flex-direction:row-reverse}
</style>
</head>
<body>
<main class="board">

  <section class="cell">
    <div class="spread">
      <div class="page page--left page--dark">
        <div class="map-block map-block--light" role="img" aria-label="Map silhouette of Latin America"></div>
      </div>
      <div class="page page--dark">
        <div class="brand brand--cover brand--light"><span class="brand__dot"></span><span>Andes Pantry<br>Company</span></div>
      </div>
    </div>
    <p class="caption">Opción tapa 1</p>
  </section>

  <section class="cell">
    <div class="spread">
      <div class="page page--left">
        <div class="map-block map-block--dark" role="img" aria-label="Map silhouette of Latin America"></div>
      </div>
      <div class="page">
        <div class="brand brand--cover brand--dark"><span class="brand__dot"></span><span>Andes Pantry<br>Company</span></div>
      </div>
    </div>
    <p class="caption">Opción tapa 2</p>
  </section>

  <section class="cell">
    <div class="spread">
      <div class="page page--left">
        <div class="photo photo--corn" role="img" aria-label="Photo of colourful Andean corn cobs"></div>
      </div>
      <div class="page">
        <h2 class="heading-serif index__title">Welcome</h2>
        <ul class="index__list index__list--a">
          <li>Our story</li><li>Our values</li><li>Our brands</li><li>Our partners</li><li>Our markets</li>
        </ul>
        <ul class="index__list index__list--b">
          <li>Sauces</li><li>Snacks</li><li>Beverages</li><li>Sweets</li><li>Contact</li>
        </ul>
        <span class="index__side">contents</span>
        <div class="brand brand--corner"><span>Andes Pantry Company</span><span class="brand__dot"></span></div>
      </div>
    </div>
    <p class="caption">Indice</p>
  </section>

  <section class="cell">
    <div class="spread">
      <div class="page page--left page--framed">
        <h2 class="heading-serif story__title">Our Story</h2>
        <span class="story__rule"></span>
        <p class="body-copy story__copy">Founded to bring the finest Latin American pantry to Europe, we work directly with producers from Argentina to Mexico, selecting premium brands that honour tradition, origin and quality in every product we import.</p>
      </div>
      <div class="page">
        <div class="photo photo--full photo--churros" role="img" aria-label="Photo of sugared churros on newspaper"></div>
      </div>
    </div>
    <p class="caption">Historia de la empresa</p>
  </section>

  <section class="cell">
    <div class="spread">
      <div class="page page--left">
        <p class="flavors__kicker">flavors<br>of</p>
        <h2 class="flavors__title">LATIN AMERICA</h2>
        <p class="body-copy flavors__copy">Recipes shaped by mountains, coasts and markets, carried by families and brought to your shelves with care.</p>
      </div>
      <div class="page">
        <div class="photo photo--full photo--mortar" role="img" aria-label="Photo of edible flowers in a stone mortar"></div>
        <div class="brand brand--corner" style="color:#fff"><span>Andes Pantry Company</span><span class="brand__dot" style="background:#fff"></span></div>
      </div>
    </div>
    <p class="caption">Descripción de marca</p>
  </section>

  <section class="cell">
    <div class="spread">
      <div class="page page--left">
        <div class="photo photo--full photo--drink" role="img" aria-label="Photo of a salt-rimmed lime drink with lime slices"></div>
      </div>
      <div class="page">
        <div class="product product--pineapple"><span class="product__art" style="background:#e0a83a" role="img" aria-label="Pineapple"></span><p class="product__label"><strong>Pineapple</strong>Golden fruit, sweet and juicy.</p></div>
        <div class="product product--strawberry"><span class="product__art" style="background:#c8343a" role="img" aria-label="Strawberries"></span><p class="product__label"><strong>Strawberry</strong>Ripe red berries, hand picked.</p></div>
        <div class="product product--lime"><span class="product__art" style="background:#9cc04a" role="img" aria-label="Lime"></span><p class="product__label"><strong>Lime Cordial</strong>Fresh citrus for drinks.</p></div>
        <div class="product product--coconut"><span class="product__art" style="background:#8a5a3a" role="img" aria-label="Coconut"></span><p class="product__label"><strong>Coconut</strong>Creamy tropical flesh and water.</p></div>
        <div class="brand brand--corner"><span>Andes Pantry Company</span><span class="brand__dot"></span></div>
      </div>
    </div>
    <p class="caption">Catálogo de productos</p>
  </section>

</main>
</body>
</html>
```